Design new marketing postcard for mortgage loan applicants

I have provided a postcard recently designed as a possible guide for this project and have attached it. The new text is rough drafted and included. Please feel free to design outside of the old postcard or you can design close to it.

```html
<!DOCTYPE html>
<html lang="en">
<head>
<meta charset="utf-8">
<title>Cash Out Equity Loan Postcard</title>
<link href="https://fonts.googleapis.com/css2?family=Montserrat:wght@400;500;600;700;800&family=Oswald:wght@600;700&display=swap" rel="stylesheet">
<style>
  :root {
    --navy: #0f3a5f;
    --navy-light: #1c4f78;
    --red: #e0141e;
    --blue-text: #0d4a8c;
    --gold: #d2a257;
    --gold-light: #ecc98b;
    --paper: #ffffff;
    --ink: #3a3a3a;
    --rule: #c7c7c7;
    --stamp: #dcdcde;
    --bg: #e4e4e4;
  }
  * { margin: 0; padding: 0; box-sizing: border-box; }
  html, body { width: 1200px; height: 903px; overflow: hidden; background: var(--bg); }
  body { position: relative; font-family: 'Montserrat', sans-serif; }

  .card {
    position: absolute;
    width: 532px;
    height: 355px;
    background: var(--paper);
    overflow: hidden;
    box-shadow: 0 3px 10px rgba(0,0,0,0.18);
  }
  .card--front { left: 209px; top: 78px; }
  .card--back { left: 500px; top: 480px; }

  /* Front */
  .front-header { position: absolute; left: 22px; top: 19px; }
  .front-title {
    font-family: 'Oswald', sans-serif;
    font-weight: 700;
    font-size: 25px;
    line-height: 1;
    color: var(--red);
    letter-spacing: 0.2px;
    transform: scaleY(1.05);
    transform-origin: left top;
  }
  .front-subtitle {
    margin-top: 4px;
    font-weight: 700;
    font-size: 12.2px;
    color: var(--blue-text);
    letter-spacing: 0.2px;
  }
  .benefit-panel {
    position: absolute;
    left: 0; top: 69px;
    width: 300px; height: 129px;
    background: linear-gradient(180deg, var(--navy) 0%, var(--navy-light) 100%);
  }
  .benefit-list {
    list-style: none;
    position: absolute;
    left: 21px; top: 12px;
  }
  .benefit-list li {
    display: flex;
    align-items: center;
    gap: 9px;
    height: 22px;
    font-weight: 500;
    font-size: 12.3px;
    color: #fff;
    letter-spacing: 0.2px;
  }
  .benefit-list svg { width: 8px; height: 8px; flex: none; }

  .front-brand {
    position: absolute;
    left: 30px; top: 214px;
    display: flex;
    align-items: center;
    gap: 8px;
  }
  .brand-mark { width: 16px; height: 16px; border-radius: 50%; background: var(--gold); flex: none; }
  .brand-name {
    font-weight: 700;
    font-size: 12px;
    line-height: 1.15;
    color: var(--navy);
    letter-spacing: 0.3px;
  }
  .front-nmls {
    position: absolute;
    left: 54px; top: 258px;
    font-weight: 500;
    font-size: 13.5px;
    color: var(--navy);
    letter-spacing: 0.5px;
  }
  .photo { position: absolute; left: 0; top: 0; width: 532px; height: 290px; }

  .call-band {
    position: absolute;
    left: 0; top: 287px;
    width: 532px; height: 68px;
    background: var(--navy);
    border-top: 2px solid var(--gold);
    display: flex;
    align-items: center;
    padding-left: 21px;
    color: #fff;
    font-weight: 700;
  }
  .call-band .call-label { font-size: 39px; letter-spacing: 1.5px; }
  .call-band .call-icon { width: 34px; height: 34px; margin: 0 26px 0 22px; }
  .call-band .call-number { font-size: 40px; letter-spacing: 1px; }

  /* Back */
  .back-curve { position: absolute; left: 0; top: 0; width: 532px; height: 355px; }
  .back-message {
    position: absolute;
    left: 22px; top: 33px;
    width: 240px;
    font-size: 10.9px;
    line-height: 13.4px;
    color: var(--ink);
    letter-spacing: 0.3px;
  }
  .back-disclaimer {
    position: absolute;
    left: 22px; top: 152px;
    width: 245px;
    font-size: 9.1px;
    line-height: 11.8px;
    color: var(--ink);
    text-align: justify;
    letter-spacing: 0.2px;
  }
  .back-call {
    position: absolute;
    left: 22px; top: 314px;
    display: flex;
    align-items: center;
    color: #fff;
    font-weight: 700;
  }
  .back-call .call-label { font-size: 19px; letter-spacing: 1px; }
  .back-call .call-icon { width: 19px; height: 19px; margin: 0 13px 0 14px; }
  .back-call .call-number { font-size: 19px; letter-spacing: 0.6px; }
  .back-brand {
    position: absolute;
    left: 296px; top: 58px;
    display: flex;
    align-items: center;
    gap: 7px;
  }
  .back-brand .brand-name { font-size: 10.5px; }
  .back-brand .brand-mark { width: 14px; height: 14px; }
  .stamp-box {
    position: absolute;
    left: 458px; top: 22px;
    width: 52px; height: 61px;
    background: var(--stamp);
  }
  .address-line {
    position: absolute;
    left: 304px;
    width: 206px;
    height: 1px;
    background: var(--rule);
  }
</style>
</head>
<body>

<section class="card card--front">
  <svg class="photo" viewBox="0 0 532 290" role="img" aria-label="Photo of a smiling young couple in denim shirts, the man embraced from behind by the woman">
    <defs>
      <linearGradient id="photoTone" x1="0" y1="0" x2="0.6" y2="1">
        <stop offset="0" stop-color="#c9d2dc"/>
        <stop offset="0.55" stop-color="#a9bdd2"/>
        <stop offset="1" stop-color="#6e9ac6"/>
      </linearGradient>
    </defs>
    <path d="M278 0 Q196 150 252 290 L532 290 L532 0 Z" fill="url(#photoTone)"/>
    <path d="M278 0 Q196 150 252 290" fill="none" stroke="#d2a257" stroke-width="4"/>
  </svg>

  <header class="front-header">
    <h1 class="front-title">CASH OUT EQUITY LOAN</h1>
    <p class="front-subtitle">ON YOUR INVESTMENT PROPERTY</p>
  </header>

  <div class="benefit-panel">
    <ul class="benefit-list">
      <li><svg viewBox="0 0 10 10"><circle cx="5" cy="5" r="5" fill="#d2a257"/><path d="M2.6 5.2 L4.3 6.8 L7.4 3.6" stroke="#0f3a5f" stroke-width="1.4" fill="none"/></svg>Loan Based on your equity</li>
      <li><svg viewBox="0 0 10 10"><circle cx="5" cy="5" r="5" fill="#d2a257"/><path d="M2.6 5.2 L4.3 6.8 L7.4 3.6" stroke="#0f3a5f" stroke-width="1.4" fill="none"/></svg>Fast close</li>
      <li><svg viewBox="0 0 10 10"><circle cx="5" cy="5" r="5" fill="#d2a257"/><path d="M2.6 5.2 L4.3 6.8 L7.4 3.6" stroke="#0f3a5f" stroke-width="1.4" fill="none"/></svg>No Income Qualifying</li>
      <li><svg viewBox="0 0 10 10"><circle cx="5" cy="5" r="5" fill="#d2a257"/><path d="M2.6 5.2 L4.3 6.8 L7.4 3.6" stroke="#0f3a5f" stroke-width="1.4" fill="none"/></svg>Not based on credit scores</li>
      <li><svg viewBox="0 0 10 10"><circle cx="5" cy="5" r="5" fill="#d2a257"/><path d="M2.6 5.2 L4.3 6.8 L7.4 3.6" stroke="#0f3a5f" stroke-width="1.4" fill="none"/></svg>Competstive Rates</li>
    </ul>
  </div>

  <div class="front-brand">
    <span class="brand-mark"></span>
    <span class="brand-name">HARBORLINE<br>LENDING, INC.</span>
  </div>
  <p class="front-nmls">NMLS #418907</p>

  <div class="call-band">
    <span class="call-label">CALL</span>
    <svg class="call-icon" viewBox="0 0 24 24"><path d="M6.6 2.5 L9.2 6.8 L7.4 8.7 Q9 12.6 12.8 14.8 L14.8 13 L19 15.7 L17.6 19.4 Q16.6 20.5 14.8 20 Q6.2 16.6 3.6 8.6 Q3.2 6.6 4.4 5.6 Z" fill="#e0141e"/><path d="M14 3.5 A7 7 0 0 1 20.5 10" stroke="#e0141e" stroke-width="1.8" fill="none"/><path d="M13.6 7 A3.8 3.8 0 0 1 17.2 10.6" stroke="#e0141e" stroke-width="1.8" fill="none"/></svg>
    <span class="call-number">800-555-0142</span>
  </div>
</section>

<section class="card card--back">
  <svg class="back-curve" viewBox="0 0 532 355" aria-hidden="true">
    <path d="M236 0 Q305 120 276 284" fill="none" stroke="#d2a257" stroke-width="4"/>
    <path d="M0 292 L280 292 Q264 340 252 355 L0 355 Z" fill="#0f3a5f"/>
  </svg>

  <p class="back-message">I am pleased to inform you that an equity based loan is available for your investment property. This no qualifying loan is possible simple due to the equity you have. Please call for a quote. You can also email dan@harborline.loan</p>

  <p class="back-disclaimer">*Loan is subject to confirmation of equity and is for income property, investment property, rental property business purpose only. Other conditions and restrictions apply. Please call for complete program requirements and details. Harborline Lending, Inc. 2280 Harbor View Dr. Suite 210, Bayview CA 94011, Harborline CA Dept of Real Estate-Real Estate Broker Lic.#02954410,NMLS # 506321, CA Dept. of real estate Lic.# 02761935,NMLS #418907.</p>

  <div class="back-call">
    <span class="call-label">CALL</span>
    <svg class="call-icon" viewBox="0 0 24 24"><path d="M6.6 2.5 L9.2 6.8 L7.4 8.7 Q9 12.6 12.8 14.8 L14.8 13 L19 15.7 L17.6 19.4 Q16.6 20.5 14.8 20 Q6.2 16.6 3.6 8.6 Q3.2 6.6 4.4 5.6 Z" fill="#e0141e"/><path d="M14 3.5 A7 7 0 0 1 20.5 10" stroke="#e0141e" stroke-width="1.8" fill="none"/><path d="M13.6 7 A3.8 3.8 0 0 1 17.2 10.6" stroke="#e0141e" stroke-width="1.8" fill="none"/></svg>
    <span class="call-number">800-555-0142</span>
  </div>

  <div class="back-brand">
    <span class="brand-mark"></span>
    <span class="brand-name">HARBORLINE<br>LENDING, INC.</span>
  </div>

  <div class="stamp-box"></div>
  <div class="address-line" style="top:166px"></div>
  <div class="address-line" style="top:205px"></div>
  <div class="address-line" style="top:244px"></div>
</section>

</body>
</html>
```